QUIVR

We provide order application for restaurants.
We need something modern, with a real visual identity.
it must be a landscape format.
Here our website: www.quivr.example
a mix between those two leaflet would be great:
https://brindle.folioshare.example/share/XmTq7bLp2Rz9WvKc4Hn3d/1
(landscape format)
https://app.leadnest.example/documents/4172093/view/519204716?accessId=3fa91d

IMPORTANT: this is not for taking. it's a leaflet to share by mail. (7 - 8 pages max)

Industry/Entity Type

web developement

Colors
6B429C
8869AF
B7A5CE
E3DAEB
F3F0F8

Requirements
Must have
• landscape format, to send by email (not for print).

```html
<!DOCTYPE html>
<html lang="en">
<head>
<meta charset="utf-8">
<title>QUIVR – Restaurant Ordering App Leaflet</title>
<link href="https://fonts.googleapis.com/css2?family=Montserrat:wght@300;400;600;700;800&family=Roboto:wght@300;400;500&display=swap" rel="stylesheet">
<style>
  :root{
    --purple-deep:#6B429C;
    --purple:#8869AF;
    --purple-soft:#B7A5CE;
    --lavender:#E3DAEB;
    --mist:#F3F0F8;
    --ink:#141418;
    --ink-2:#1d1c23;
    --ink-3:#2a2833;
    --white:#ffffff;
    --text-muted:#c9c4d3;
  }
  *{box-sizing:border-box;margin:0;padding:0}
  html,body{width:1200px;height:5140px;overflow:hidden;background:var(--mist)}
  body{font-family:"Roboto",Arial,sans-serif;color:var(--white)}
  .leaflet{position:relative;width:1200px;height:5140px}
  .page{position:absolute;left:0;width:1200px;height:840px;overflow:hidden;
    background:linear-gradient(135deg,var(--ink-2) 0%,var(--ink) 55%,var(--ink-3) 100%)}
  .page--1{top:0}.page--2{top:860px}.page--3{top:1720px}
  .page--4{top:2580px}.page--5{top:3440px}.page--6{top:4300px}
  .page-art{position:absolute;inset:0;width:1200px;height:840px}
  .abs{position:absolute}
  .heading-light{font-family:"Montserrat",Arial,sans-serif;font-weight:300;letter-spacing:4px;text-transform:uppercase}
  .heading-bold{font-family:"Montserrat",Arial,sans-serif;font-weight:800;text-transform:uppercase;letter-spacing:1px}
  .body-copy{font-size:17px;line-height:1.55;color:var(--text-muted)}

  /* Page 1 */
  .brand{right:70px;top:150px}
  .brand-name{font-family:"Montserrat",Arial,sans-serif;font-weight:700;font-size:30px;letter-spacing:4px}
  .cover-title{right:50px;top:470px;text-align:right}
  .cover-title .line-1{font-size:48px}
  .cover-title .line-2{font-size:78px;line-height:1.05;color:var(--lavender)}
  .cover-title .line-3{font-size:40px}
  .cover-copy{right:50px;top:712px;text-align:right;font-size:17px;line-height:2.4;color:var(--text-muted)}

  /* Page 2 */
  .features-kicker{left:400px;top:40px;font-size:28px}
  .features-title{left:400px;top:76px;font-size:50px}
  .feature-list{left:400px;top:160px;list-style:none;width:560px}
  .feature{position:relative;height:102px}
  .feature-icon{display:block;width:34px;height:30px;margin-bottom:4px}
  .feature-name{font-family:"Montserrat",Arial,sans-serif;font-weight:700;font-size:26px;text-transform:uppercase;line-height:1}
  .feature-text{font-size:17px;color:var(--text-muted);margin-top:6px}
  .panel-note{width:150px;font-size:12px;line-height:1.35;color:var(--lavender)}
  .panel-note strong{display:block;font-size:15px;color:var(--white);font-weight:500;margin-bottom:4px}

  /* Page 3 */
  .turnkey-title{left:40px;top:42px;font-size:56px}
  .turnkey-title span{font-weight:300}
  .turnkey-intro{left:40px;top:122px;width:560px}
  .service-list{left:280px;top:220px;list-style:none;width:520px}
  .service{display:flex;gap:34px;height:88px}
  .service-icon{flex:0 0 40px;height:40px;margin-top:2px}
  .service-name{font-family:"Montserrat",Arial,sans-serif;font-weight:700;font-size:22px;text-transform:uppercase}
  .service-text{font-size:13px;line-height:1.4;color:var(--text-muted);margin-top:4px}

  /* Page 4 */
  .why-title{right:40px;top:70px;text-align:right;font-size:46px;line-height:1.1}
  .why-sub{right:40px;top:190px;text-align:right;font-family:"Montserrat",Arial,sans-serif;font-weight:700;font-size:26px;text-transform:uppercase}
  .why-copy{right:40px;top:228px;width:480px;text-align:right}
  .coaching-title{right:40px;top:450px;text-align:right;font-size:56px}
  .coaching-title span{font-weight:300}
  .coaching-copy{right:40px;top:528px;width:480px;text-align:right}

  /* Page 5 */
  .control-title{left:80px;top:40px;font-size:52px;line-height:1.05}
  .control-title span{font-weight:300}
  .control-copy{left:80px;top:152px;width:720px}
  .coaching-badge{left:160px;top:400px;width:380px;text-align:center}
  .coaching-badge .heading-bold{font-size:40px;line-height:1.05;margin-top:14px}
  .coaching-badge .body-copy{color:var(--white);font-size:16px;margin-top:14px}

  /* Page 6 */
  .contact{left:610px;top:350px;width:540px}
  .contact-title{font-size:42px;margin-bottom:26px}
  .contact-list{list-style:none}
  .contact-item{display:flex;align-items:center;gap:14px;height:44px;font-size:17px}
  .contact-dot{width:16px;height:16px;border-radius:50%;background:var(--white);flex:0 0 16px}
</style>
</head>
<body>
<main class="leaflet">

  <!-- Page 1: cover -->
  <section class="page page--1">
    <svg class="page-art" viewBox="0 0 1200 840">
      <defs>
        <linearGradient id="suitGrad" x1="0" y1="0" x2="1" y2="1">
          <stop offset="0" stop-color="#5a5d66"/><stop offset=".55" stop-color="#2b2c33"/><stop offset="1" stop-color="#141418" stop-opacity="0"/>
        </linearGradient>
      </defs>
      <rect x="620" y="0" width="580" height="540" fill="url(#suitGrad)" role="img" aria-label="Photo of a businessman in a suit holding a tablet"/>
      <polygon points="0,300 330,840 0,840" fill="var(--ink-3)"/>
      <polygon points="60,120 360,620 -240,620" fill="none" stroke="var(--white)" stroke-width="14"/>
      <polygon points="0,420 250,840 0,840" fill="var(--purple-deep)"/>
      <polygon points="380,520 560,840 200,840" fill="none" stroke="var(--white)" stroke-width="10"/>
      <polygon points="470,0 640,0 555,150" fill="var(--purple)"/>
      <polygon points="0,0 260,0 0,240" fill="#0e0e12"/>
      <polygon points="760,560 880,560 820,660" fill="none" stroke="var(--purple-soft)" stroke-width="6"/>
    </svg>
    <div class="abs brand"><span class="brand-name">QUIVR</span></div>
    <h1 class="abs cover-title">
      <span class="heading-light line-1" style="display:block">Together let's</span>
      <span class="heading-bold line-2" style="display:block">Create your</span>
      <span class="heading-light line-3" style="display:block">Application</span>
    </h1>
    <p class="abs cover-copy">Your customers are looking for your app on the App Market or Play Market.<br>Your application will be constantly visible on the mobile of your customers.</p>
  </section>

  <!-- Page 2: features -->
  <section class="page page--2">
    <svg class="page-art" viewBox="0 0 1200 840">
      <polygon points="0,0 380,0 0,840" fill="var(--purple-deep)"/>
      <polygon points="0,0 330,0 0,330" fill="var(--purple)" opacity=".55"/>
      <polygon points="0,40 290,40 0,300" fill="var(--purple-soft)" opacity=".35" role="img" aria-label="Phone showing the restaurant ordering app"/>
      <polygon points="0,320 300,320 0,580" fill="var(--purple)" opacity=".5" role="img" aria-label="Phone showing order statistics"/>
      <polygon points="0,600 260,600 0,840" fill="var(--purple-soft)" opacity=".4" role="img" aria-label="Phone showing marketing tools"/>
      <polygon points="300,0 380,0 340,70" fill="var(--white)"/>
      <polygon points="1010,80 1200,80 1200,420" fill="none" stroke="var(--white)" stroke-width="8"/>
      <polygon points="1200,460 1200,840 960,840" fill="var(--ink-3)"/>
      <polygon points="1060,560 1200,560 1130,680" fill="var(--purple-deep)"/>
      <polygon points="900,0 1040,0 970,120" fill="var(--purple)" opacity=".7"/>
    </svg>
    <div class="abs panel-note" style="left:110px;top:120px"><strong>My next step</strong>Simply launch a mobile app that puts your restaurant in hand.</div>
    <div class="abs panel-note" style="left:40px;top:380px"><strong>My turnover boosted</strong>More orders, higher baskets, a powerful tool.</div>
    <div class="abs panel-note" style="left:90px;top:700px"><strong>My marketing coach</strong>Our experts are at your side to optimize your digital visibility.</div>

    <p class="abs heading-light features-kicker">Simplicity at your fingertips</p>
    <h2 class="abs heading-bold features-title">Discover your features</h2>
    <ul class="abs feature-list">
      <li class="feature">
        <svg class="feature-icon" viewBox="0 0 34 30"><rect x="2" y="8" width="20" height="14" fill="none" stroke="#fff" stroke-width="2"/><path d="M22 12h7l4 5v5h-11z" fill="none" stroke="#fff" stroke-width="2"/><circle cx="9" cy="25" r="3" fill="#fff"/><circle cx="27" cy="25" r="3" fill="#fff"/></svg>
        <div class="feature-name">A controlled delivery</div><p class="feature-text">Set a minimum order amount per sector.</p></li>
      <li class="feature">
        <svg class="feature-icon" viewBox="0 0 34 30"><rect x="3" y="18" width="6" height="10" fill="#fff"/><rect x="13" y="10" width="6" height="18" fill="#fff"/><rect x="23" y="4" width="6" height="24" fill="#fff"/></svg>
        <div class="feature-name">Statistics</div><p class="feature-text">Analyze your orders and adapt your offer.</p></li>
      <li class="feature">
        <svg class="feature-icon" viewBox="0 0 34 30"><rect x="2" y="6" width="30" height="20" rx="2" fill="none" stroke="#fff" stroke-width="2"/><rect x="2" y="11" width="30" height="4" fill="#fff"/></svg>
        <div class="feature-name">Make buying easier</div><p class="feature-text">A simplified ordering process thanks to registered means of payment.</p></li>
      <li class="feature">
        <svg class="feature-icon" viewBox="0 0 34 30"><rect x="9" y="2" width="16" height="26" rx="2" fill="none" stroke="#fff" stroke-width="2"/><circle cx="17" cy="24" r="1.6" fill="#fff"/></svg>
        <div class="feature-name">User experience</div><p class="feature-text">Ergonomic and intuitive navigation designed for mobiles.</p></li>
      <li class="feature">
        <svg class="feature-icon" viewBox="0 0 34 30"><polygon points="17,2 21,11 31,12 23,18 26,28 17,22 8,28 11,18 3,12 13,11" fill="#fff"/></svg>
        <div class="feature-name">Stand out</div><p class="feature-text">Outrun your competitors with an innovative digital tool.</p></li>
      <li class="feature">
        <svg class="feature-icon" viewBox="0 0 34 30"><path d="M6 10h22l-2 18H8z" fill="none" stroke="#fff" stroke-width="2"/><path d="M12 10V6a5 5 0 0 1 10 0v4" fill="none" stroke="#fff" stroke-width="2"/></svg>
        <div class="feature-name">Click &amp; Collect</div><p class="feature-text">Your customers choose delivery or Click &amp; Collect.</p></li>
    </ul>
  </section>

  <!-- Page 3: turnkey solution -->
  <section class="page page--3">
    <svg class="page-art" viewBox="0 0 1200 840">
      <defs>
        <linearGradient id="roomGrad" x1="0" y1="0" x2="1" y2="1"><stop offset="0" stop-color="#6f5a49"/><stop offset="1" stop-color="#2d2622"/></linearGradient>
        <linearGradient id="dishGrad" x1="0" y1="0" x2="1" y2="1"><stop offset="0" stop-color="#c9a27a"/><stop offset=".5" stop-color="#7a5a3e"/><stop offset="1" stop-color="#2a2220"/></linearGradient>
        <linearGradient id="chefGrad" x1="0" y1="0" x2="1" y2="1"><stop offset="0" stop-color="#5b4a3e"/><stop offset="1" stop-color="#1c1a1d"/></linearGradient>
      </defs>
      <polygon points="760,0 1200,0 1200,330" fill="url(#roomGrad)" role="img" aria-label="Photo of a warmly lit restaurant dining room"/>
      <polygon points="1200,200 1200,840 720,840" fill="url(#dishGrad)" role="img" aria-label="Photo of a plated gourmet dish"/>
      <polygon points="0,330 320,840 0,840" fill="url(#chefGrad)" role="img" aria-label="Photo of a chef's hands plating food"/>
      <polygon points="0,560 170,840 0,840" fill="var(--purple-deep)" opacity=".85"/>
      <polygon points="880,300 1040,300 960,440" fill="var(--purple)"/>
      <polygon points="850,560 950,560 900,650" fill="none" stroke="var(--white)" stroke-width="8"/>
      <polygon points="1100,720 1200,720 1200,840" fill="var(--purple-deep)"/>
    </svg>
    <h2 class="abs heading-bold turnkey-title">A turnkey <span>solution</span></h2>
    <p class="abs body-copy turnkey-intro">Launch the application of YOUR restaurant in the best conditions. QUIVR provides you with a complete launch pack for guaranteed success.</p>
    <ul class="abs service-list">
      <li class="service">
        <svg class="service-icon" viewBox="0 0 40 40"><rect x="12" y="4" width="16" height="32" rx="2" fill="none" stroke="#fff" stroke-width="2"/></svg>
        <div><div class="service-name">Mobile app</div><p class="service-text">Your mobile application available on the Play Market and the App Market.</p></div></li>
      <li class="service">
        <svg class="service-icon" viewBox="0 0 40 40"><rect x="4" y="8" width="32" height="22" fill="none" stroke="#fff" stroke-width="2"/><rect x="10" y="32" width="20" height="3" fill="#fff"/></svg>
        <div><div class="service-name">Admin-panel</div><p class="service-text">A tablet with an intuitive interface to manage your application (updating the offer, setting up commercial action, sending push notifications, statistics).</p></div></li>
      <li class="service">
        <svg class="service-icon" viewBox="0 0 40 40"><rect x="4" y="6" width="32" height="22" fill="none" stroke="#fff" stroke-width="2"/><polygon points="17,12 25,17 17,22" fill="#fff"/></svg>
        <div><div class="service-name">Training</div><p class="service-text">Launch training and video tutorials to master your interface.</p></div></li>
      <li class="service">
        <svg class="service-icon" viewBox="0 0 40 40"><rect x="6" y="6" width="28" height="28" fill="none" stroke="#fff" stroke-width="2"/><path d="M22 34l12-12" stroke="#fff" stroke-width="2"/></svg>
        <div><div class="service-name">Decals</div><p class="service-text">App Market and Play Market sticker to stick on your shop window.</p></div></li>
      <li class="service">
        <svg class="service-icon" viewBox="0 0 40 40"><path d="M6 16h8l14-8v24l-14-8H6z" fill="#fff"/></svg>
        <div><div class="service-name">Digital-marketing</div><p class="service-text">Graphic creation of three posts on your social networks and a teasing video (20 sec) to promote your application.</p></div></li>
      <li class="service">
        <svg class="service-icon" viewBox="0 0 40 40"><path d="M10 4h14l8 8v24H10z" fill="none" stroke="#fff" stroke-width="2"/></svg>
        <div><div class="service-name">Flyer</div><p class="service-text">Creation of 500 personalized flyers with the integration of the QR code for direct download of the application.</p></div></li>
    </ul>
  </section>

  <!-- Page 4: why an app -->
  <section class="page page--4">
    <svg class="page-art" viewBox="0 0 1200 840">
      <defs>
        <radialGradient id="appsGrad" cx=".45" cy=".4" r=".7"><stop offset="0" stop-color="#9d86c4"/><stop offset=".5" stop-color="#3b3450"/><stop offset="1" stop-color="#141418"/></radialGradient>
      </defs>
      <polygon points="0,0 640,0 420,840 0,840" fill="url(#appsGrad)" role="img" aria-label="Illustration of app icons bursting out of a smartphone"/>
      <polygon points="560,0 700,0 630,120" fill="var(--purple-deep)"/>
      <polygon points="0,680 180,840 0,840" fill="var(--purple)"/>
      <polygon points="1200,620 1200,840 960,840" fill="var(--purple-deep)"/>
      <polygon points="1060,700 1200,700 1130,820" fill="none" stroke="var(--white)" stroke-width="8"/>
    </svg>
    <h2 class="abs heading-light why-title">Why an app for your<br><b style="font-weight:800">restaurant?</b></h2>
    <p class="abs why-sub">A turnover doubled!</p>
    <p class="abs body-copy why-copy">Thanks to a customer conversion rate 3 times higher than the web, the mobile application allows our partner restaurateurs to multiply orders and increase the value of the average basket. Your personal application, the ideal showcase to boost your business!</p>
    <h2 class="abs heading-bold coaching-title">Digital <span>coaching</span></h2>
    <p class="abs body-copy coaching-copy">To give your application maximum visibility, our team is at your side to develop and guide your digital strategy. Promotional operations, loyalty programs, communication on social networks and advertising (Print and Web) are all levers of action to lead you to success.</p>
  </section>

  <!-- Page 5: full control -->
  <section class="page page--5">
    <svg class="page-art" viewBox="0 0 1200 840">
      <defs>
        <linearGradient id="phoneGrad" x1="0" y1="0" x2="1" y2="1"><stop offset="0" stop-color="#4a4656"/><stop offset=".6" stop-color="#24222b"/><stop offset="1" stop-color="#101013"/></linearGradient>
      </defs>
      <polygon points="760,280 1200,280 1200,840 600,840" fill="url(#phoneGrad)" role="img" aria-label="Photo of a smartphone screen full of app icons"/>
      <polygon points="340,280 680,840 0,840" fill="var(--purple-deep)"/>
      <polygon points="340,230 740,840 -60,840" fill="none" stroke="var(--white)" stroke-width="10"/>
      <polygon points="1000,0 1200,0 1200,220" fill="var(--purple)" opacity=".8"/>
      <polygon points="0,0 60,0 0,90" fill="var(--white)"/>
    </svg>
    <h2 class="abs heading-bold control-title">Your application in<br><span>full control</span></h2>
    <p class="abs body-copy control-copy">Via a tablet or a smartphone with a dedicated application, you fully exploit the potential of your application. You will then be able to: Manage your orders, manage your products, send a personalized notification, define delivery zones.</p>
    <div class="abs coaching-badge">
      <svg width="70" height="60" viewBox="0 0 40 34"><path d="M4 12h8l18-10v30L12 22H4z" fill="#fff"/><rect x="8" y="22" width="5" height="10" fill="#fff"/></svg>
      <h3 class="heading-bold">Digital<br>coaching</h3>
      <p class="body-copy">To give your application maximum visibility, our team is at your side to develop and guide your digital strategy. Promotional operations, loyalty programs, communication on social networks and advertising (Print and Web) are all levers of action to lead you to success.</p>
    </div>
  </section>

  <!-- Page 6: contact -->
  <section class="page page--6">
    <svg class="page-art" viewBox="0 0 1200 840">
      <defs>
        <linearGradient id="foodGrad" x1="0" y1="0" x2="1" y2="1"><stop offset="0" stop-color="#b98a5e"/><stop offset=".5" stop-color="#6a4c36"/><stop offset="1" stop-color="#221c1c"/></linearGradient>
      </defs>
      <rect x="0" y="0" width="760" height="840" fill="url(#foodGrad)" role="img" aria-label="Photo of a gourmet plated dish"/>
      <polygon points="0,0 200,0 0,260" fill="var(--ink)"/>
      <polygon points="440,840 1200,0 1200,840" fill="var(--purple-deep)"/>
      <polygon points="560,120 1200,120 1200,840 560,840" fill="var(--purple-deep)" opacity=".35"/>
      <polygon points="980,0 1200,0 1200,260" fill="var(--ink)"/>
      <polygon points="200,700 320,700 260,800" fill="none" stroke="var(--white)" stroke-width="8"/>
      <polygon points="0,620 160,840 0,840" fill="var(--purple)"/>
    </svg>
    <div class="abs contact">
      <h2 class="heading-bold contact-title">Contact info</h2>
      <ul class="contact-list">
        <li class="contact-item"><span class="contact-dot"></span>(0100)-555-204</li>
        <li class="contact-item"><span class="contact-dot"></span>www.quivr.example</li>
        <li class="contact-item"><span class="contact-dot"></span>https://chirpline.example/QuivrHQ</li>
        <li class="contact-item"><span class="contact-dot"></span>https://www.facetome.example/quivr.agency</li>
        <li class="contact-item"><span class="contact-dot"></span>https://www.snapgrid.example/quivr_agency/</li>
        <li class="contact-item"><span class="contact-dot"></span>https://www.worklink.example/company/quivr-agency/</li>
        <li class="contact-item"><span class="contact-dot"></span>https://www.viewtube.example/channel/QvR7mXpL2sTa9</li>
      </ul>
    </div>
  </section>

</main>
</body>
</html>
```